Business Card Design for BT Wine:

I'm looking for a card that has the following.
Front:
- Merlot Colored
- stripe down the middle in silver or gold flake
- BT in block like thick letters with gold or silver flake above stripe
-Wine: below stripe
- a grape bunch that is at the end of the stripe that is made so it can be printed as embossed
Back:
- line down the middle of card in Merlot, card is white background
- to the left Marla Boyce, (next line) Owner, (next line) Certified Sommelier, GRV
- to the right (listed) restaurant consulting, wine tours, personal tastings, event planning, personal wine buying
- add embossed grape bunch
Also, looking for a piece that slides over like a envelope for a room key for a hotel that says "We met @ DUNVAL" and possibly a file for that, that I can edit.
Would like card to be printed on a thicker cardstock

```html
<!DOCTYPE html>
<html lang="en">
<head>
<meta charset="utf-8">
<title>BT Wine — Business Card</title>
<link rel="stylesheet" href="https://fonts.googleapis.com/css2?family=Cinzel:wght@400&family=Open+Sans:wght@400;600;700;800&display=swap">
<style>
  :root {
    --merlot: #4e0012;
    --merlot-deep: #3f000e;
    --gold: #dba628;
    --silver-light: #f4f4f4;
    --silver-mid: #c9c9c9;
    --silver-dark: #9a9a9a;
    --card-white: #f1f1f1;
    --ink: #2b2b2b;
    --backdrop: #e6e2de;
  }
  * { margin: 0; padding: 0; box-sizing: border-box; }
  html, body {
    width: 1200px; height: 900px; overflow: hidden;
    background: var(--backdrop);
  }
  .canvas { position: relative; width: 1200px; height: 900px; }

  .card { position: absolute; box-shadow: 0 6px 18px rgba(0,0,0,0.18); }

  /* Front */
  .card-front {
    left: 125px; top: 62px; width: 588px; height: 363px;
    background: var(--merlot);
  }
  .brand-mark {
    position: absolute; left: 187px; top: 70px;
    font-family: "Open Sans", sans-serif; font-weight: 800;
    font-size: 100px; line-height: 1; letter-spacing: 4px;
    color: var(--gold);
  }
  .silver-stripe {
    position: absolute; left: 0; top: 185px; width: 100%; height: 20px;
    background: linear-gradient(to bottom, var(--silver-light) 0%, var(--silver-mid) 55%, var(--silver-dark) 100%);
  }
  .brand-word {
    position: absolute; left: 220px; top: 223px;
    font-family: "Cinzel", serif; font-size: 32px;
    letter-spacing: 14px; color: #ffffff;
  }
  .grape-emboss {
    position: absolute; left: 402px; top: 203px; width: 143px; height: 137px;
    border-radius: 40% 40% 50% 50%;
    background: radial-gradient(circle at 40% 40%, #5e0a1e 0%, var(--merlot-deep) 75%);
  }

  /* Back */
  .card-back {
    left: 388px; top: 466px; width: 567px; height: 352px;
    background: var(--card-white);
  }
  .center-rule {
    position: absolute; left: 247px; top: 0; width: 2px; height: 100%;
    background: var(--merlot);
  }
  .contact {
    position: absolute; left: 40px; top: 135px;
    font-family: "Open Sans", sans-serif; color: var(--ink);
  }
  .contact-name {
    font-weight: 700; font-size: 19px; color: var(--merlot);
    margin-bottom: 4px; line-height: 1.2;
  }
  .contact-line { font-size: 15px; line-height: 23px; }
  .services {
    position: absolute; left: 275px; top: 126px; list-style: none;
    font-family: "Open Sans", sans-serif; font-size: 15px;
    line-height: 20.7px; color: var(--ink);
  }
  .services li { position: relative; padding-left: 17px; }
  .services li::before {
    content: ""; position: absolute; left: 0; top: 6px;
    width: 8px; height: 8px; border-radius: 50%; background: var(--merlot);
  }
  .grape-emboss-light {
    position: absolute; left: 430px; top: 206px; width: 122px; height: 116px;
    border-radius: 40% 40% 50% 50%;
    background: radial-gradient(circle at 40% 40%, #fafafa 0%, #dcdcdc 80%);
  }
</style>
</head>
<body>
<main class="canvas">
  <section class="card card-front">
    <div class="brand-mark">BT</div>
    <div class="silver-stripe"></div>
    <div class="brand-word">WINE</div>
    <div class="grape-emboss" role="img" aria-label="Embossed grape bunch with vine leaf"></div>
  </section>

  <section class="card card-back">
    <div class="center-rule"></div>
    <div class="contact">
      <p class="contact-name">MARLA BOYCE</p>
      <p class="contact-line">Owner</p>
      <p class="contact-line">Certified Sommelier, GRV</p>
    </div>
    <ul class="services">
      <li>Restaurant Consulting</li>
      <li>Wine Tours</li>
      <li>Personal Tastings</li>
      <li>Event Planning</li>
      <li>Personal wine buying</li>
    </ul>
    <div class="grape-emboss-light" role="img" aria-label="Embossed grape bunch with vine leaf"></div>
  </section>
</main>
</body>
</html>
```